new hotel menu

help me do do the graphic design for our country pub the coolabah arms in holbrook. the pub has a relaxed australian country feel. here is a copy of our current menu this has our current logo already on it. the numbers after the dishes and discriptions are the prices as i dont often like to use dollar signs. i will also add a couple of quick files that i hit feeding the menu to word mill. i like the feel but not the results. i will also add a file withthe new menu

```html
<!DOCTYPE html>
<html lang="en">
<head>
<meta charset="utf-8">
<title>The Coolabah Arms – Menu</title>
<link href="https://fonts.googleapis.com/css2?family=Josefin+Sans:ital,wght@0,400;0,600;0,700;1,600&display=swap" rel="stylesheet">
<style>
  :root{
    --backdrop:#3a3a3a;
    --paper:#e5d3b0;
    --accent:#d9573a;
    --ink:#2b2420;
    --muted-accent:rgba(217,87,58,.18);
  }
  *{box-sizing:border-box;margin:0;padding:0}
  html,body{width:1200px;height:1200px;overflow:hidden;background:var(--backdrop)}
  body{position:relative;font-family:"Josefin Sans",sans-serif;color:var(--ink)}

  .page{position:absolute;top:276px;width:458px;height:648px;background:var(--paper)}
  .page--food{left:133px}
  .page--pizza{left:609px}
  .frame{position:absolute;left:10.5px;top:11px;right:10.5px;bottom:11px;border:1.6px solid var(--accent)}
  .divider{position:absolute;left:10.5px;right:10.5px;height:1.6px;background:var(--accent)}

  .brand{position:absolute;left:150px;width:158px;top:32px;text-align:center}
  .brand__mark{display:block;width:18px;height:18px;border-radius:50%;background:var(--accent);margin:0 auto 14px}
  .brand__name{display:block;font-weight:700;font-size:15px;line-height:1.35;letter-spacing:.05em;color:var(--ink);text-transform:uppercase}
  .flourish{position:absolute;top:60px;width:100px;height:28px;border-radius:14px;background:var(--muted-accent)}
  .flourish--left{left:40px}
  .flourish--right{left:318px}

  .section-title{position:absolute;left:20px;font-weight:700;color:var(--accent);text-transform:uppercase;letter-spacing:.06em;font-size:14.5px;line-height:1}
  .section-title::before{content:"•";font-size:8px;margin-right:5px;vertical-align:3px}
  .section-title--large{font-size:23px;left:19px}
  .section-title--large::before{vertical-align:6px}
  .sub-title{position:absolute;left:31px;font-weight:600;font-size:11px;letter-spacing:.05em;text-transform:uppercase;line-height:1}

  .menu{position:absolute;left:30px;width:398px;list-style:none}
  .page--pizza .menu{left:31px;width:404px}
  .item{display:grid;grid-template-columns:18px auto 1fr 32px;align-items:center;height:11.2px;border-bottom:.8px dashed var(--accent)}
  .page--pizza .item{grid-template-columns:18px auto 1fr 22px}
  .item--tall{height:22px}
  .item--mid{height:18px}
  .item--extra{height:15px}
  .item__num{color:var(--accent);font-size:6.8px;font-weight:600}
  .item__name{font-size:7.2px;font-weight:600;letter-spacing:.05em;text-transform:uppercase;white-space:nowrap}
  .item__desc{font-size:5.6px;letter-spacing:.07em;text-transform:uppercase;text-align:right;line-height:1.2;padding-left:8px}
  .item__desc--strong{font-size:7px;font-weight:600;text-transform:none}
  .item__desc .gap{margin-right:34px;font-size:7.2px;font-weight:600}
  .item__price{font-size:7.6px;font-weight:600;text-align:center}
  .page--pizza .item__price{text-align:right}

  .note{position:absolute;left:30px;font-style:italic;font-weight:600;font-size:6px;letter-spacing:.05em;text-transform:uppercase}

  .sketch{position:absolute;border-radius:6px;background:rgba(43,36,32,.12)}
</style>
</head>
<body>

<section class="page page--food">
  <div class="frame"></div>

  <div class="flourish flourish--left" role="img" aria-label="Decorative scroll flourish"></div>
  <header class="brand">
    <span class="brand__mark"></span>
    <span class="brand__name">The Coolabah<br>Arms</span>
  </header>
  <div class="flourish flourish--right" role="img" aria-label="Decorative scroll flourish"></div>

  <h2 class="section-title" style="top:140px">Starters &amp; Shares &amp; Sides</h2>
  <ul class="menu" style="top:156px">
    <li class="item"><span class="item__num">1.</span><span class="item__name">Garlic Bread</span><span class="item__desc">Classic or with cheese &amp; bacon</span><span class="item__price">9/12</span></li>
    <li class="item"><span class="item__num">2.</span><span class="item__name">Pumpkin + Feta Arancini</span><span class="item__desc">With sage and pine nut dressing</span><span class="item__price">15</span></li>
    <li class="item"><span class="item__num">3.</span><span class="item__name">Salt &amp; Pepper Squid</span><span class="item__desc">With aioli and side salad</span><span class="item__price">15</span></li>
    <li class="item"><span class="item__num">4.</span><span class="item__name">Fried Prawn Dumplings</span><span class="item__desc">Soy &amp; sesame dressing</span><span class="item__price">15</span></li>
    <li class="item"><span class="item__num">5.</span><span class="item__name">Fries- 9 / Loaded 14/</span><span class="item__desc">Parmesan and rosemary salt</span><span class="item__price">12</span></li>
    <li class="item"><span class="item__num">6.</span><span class="item__name">Bruschetta</span><span class="item__desc">Tomato, basil, balsamic glaze on toasted garlic loaf</span><span class="item__price">13</span></li>
    <li class="item"><span class="item__num">7.</span><span class="item__name">Wedges</span><span class="item__desc">Sour cream &amp; sweet chilli sauce</span><span class="item__price">13</span></li>
    <li class="item"><span class="item__num">8.</span><span class="item__name">Mashed Potato</span><span class="item__desc">Creamy butter mash</span><span class="item__price">5</span></li>
    <li class="item"><span class="item__num">9.</span><span class="item__name">Steamed Veggies</span><span class="item__desc">Seasonal selection</span><span class="item__price">6</span></li>
    <li class="item"><span class="item__num">10.</span><span class="item__name">Garden Salad</span><span class="item__desc"></span><span class="item__price">6</span></li>
  </ul>

  <div class="divider" style="top:280px"></div>

  <h2 class="section-title" style="top:292px">Parmi Menu</h2>
  <ul class="menu" style="top:306px">
    <li class="item"><span class="item__num">1.</span><span class="item__name">Classic Parmi</span><span class="item__desc">Napoli sauce, ham, mozzarella</span><span class="item__price">9/12</span></li>
    <li class="item"><span class="item__num">2.</span><span class="item__name">Meat Lovers Parmi</span><span class="item__desc">BBQ sauce, bacon, pepperoni, ham</span><span class="item__price">15</span></li>
    <li class="item"><span class="item__num">3.</span><span class="item__name">ABC Parmi</span><span class="item__desc">Avocado, bacon, cheese</span><span class="item__price">15</span></li>
    <li class="item"><span class="item__num">4.</span><span class="item__name">Mexican Parmi</span><span class="item__desc">Salsa, jalapenos, sour cream, cheese</span><span class="item__price">15</span></li>
    <li class="item"><span class="item__num">5.</span><span class="item__name">Chook on a Hook</span><span class="item__desc">Topped with a creamy garlic prawn sauce</span><span class="item__price">12</span></li>
    <li class="item"><span class="item__num">6.</span><span class="item__name">Bushmans</span><span class="item__desc">Mushroom sauce, bacon and cheese</span><span class="item__price">13</span></li>
  </ul>
  <p class="note" style="top:381px">(All served with chips &amp; salad or mash &amp; veg)</p>

  <div class="divider" style="top:397px"></div>

  <h2 class="section-title" style="top:411px">Pub Classics &amp; Mains</h2>
  <ul class="menu" style="top:427px">
    <li class="item"><span class="item__num">1.</span><span class="item__name">Beer-Battered Fish &amp; Chips</span><span class="item__desc">Gummy shark, house-made beer batter</span><span class="item__price">24</span></li>
    <li class="item"><span class="item__num">2.</span><span class="item__name">Lamb Cutlets</span><span class="item__desc">Crumbed, served with mash and steamed greens</span><span class="item__price">28</span></li>
    <li class="item"><span class="item__num">3.</span><span class="item__name">Scotch Fillet</span><span class="item__desc"></span><span class="item__price">39</span></li>
    <li class="item"><span class="item__num">4.</span><span class="item__name">Rump Steak</span><span class="item__desc item__desc--strong">400g or 200g</span><span class="item__price">36/26</span></li>
    <li class="item item--tall"><span class="item__num">5.</span><span class="item__name">Philly Cheesesteak Burger</span><span class="item__desc">Grilled sirloin, caramelized onion,<br>swiss cheese, Arms special sauce, cheese</span><span class="item__price">26</span></li>
    <li class="item item--tall"><span class="item__num">6.</span><span class="item__name">Chicken ABC Burger</span><span class="item__desc">Avocado, bacon, sweet-chilli and cheese<br>with lettuce, sweet chilli mayo</span><span class="item__price">25</span></li>
    <li class="item item--tall"><span class="item__num">7.</span><span class="item__name">Chicken Caesar Salad</span><span class="item__desc">Grilled or crispy chicken, bacon,<br>parmesan, caesar dressing</span><span class="item__price">22</span></li>
    <li class="item"><span class="item__num">8.</span><span class="item__name">Steak Sandwich</span><span class="item__desc"></span><span class="item__price">26</span></li>
    <li class="item"><span class="item__num">9.</span><span class="item__name">Prawn and Chorizo Pasta</span><span class="item__desc"></span><span class="item__price">28</span></li>
    <li class="item"><span class="item__num">10.</span><span class="item__name">Carbonara</span><span class="item__desc"><span class="gap">24</span>Add chicken</span><span class="item__price">4</span></li>
    <li class="item"><span class="item__num">11.</span><span class="item__name">Beef and Ironbark Stout Pie</span><span class="item__desc"></span><span class="item__price">26</span></li>
    <li class="item"><span class="item__num">12.</span><span class="item__name">Bangers and Mash</span><span class="item__desc"></span><span class="item__price">22</span></li>
    <li class="item"><span class="item__num">13.</span><span class="item__name">Roast of the Day</span><span class="item__desc"></span><span class="item__price">22</span></li>
    <li class="item"><span class="item__num">14.</span><span class="item__name">Barramundi</span><span class="item__desc"></span><span class="item__price">30</span></li>
  </ul>
</section>

<section class="page page--pizza">
  <div class="frame"></div>

  <h2 class="section-title section-title--large" style="top:33px">Pizza</h2>
  <div class="sketch" style="left:382px;top:25px;width:43px;height:35px" role="img" aria-label="Line sketch of a pizza slice"></div>

  <h3 class="sub-title" style="top:63px">Classics</h3>
  <ul class="menu" style="top:75px">
    <li class="item"><span class="item__num">1.</span><span class="item__name">Margherita</span><span class="item__desc">Napoli sauce, mozzarella, fresh basil</span><span class="item__price">18</span></li>
    <li class="item"><span class="item__num">2.</span><span class="item__name">Pepperoni</span><span class="item__desc">Napoli sauce, double pepperoni, mozzarella</span><span class="item__price">22</span></li>
    <li class="item item--mid"><span class="item__num">3.</span><span class="item__name">BBQ Meat Lovers</span><span class="item__desc">Beef strips, bacon, pepperoni,<br>ham, BBQ sauce and mozzarella</span><span class="item__price">26</span></li>
    <li class="item"><span class="item__num">4.</span><span class="item__name">Hawaiian</span><span class="item__desc">Ham, pineapple, mozzarella</span><span class="item__price">24</span></li>
    <li class="item"><span class="item__num">5.</span><span class="item__name">Cheesy Garlic</span><span class="item__desc">Garlic cream base, mozzarella, oregano</span><span class="item__price">18</span></li>
    <li class="item item--mid"><span class="item__num">6.</span><span class="item__name">Supreme</span><span class="item__desc">Ham, bacon, pepperoni, red onion, olives, mushrooms,<br>pineapple and roasted capsicum on a napoli base</span><span class="item__price">26</span></li>
    <li class="item"><span class="item__num">7.</span><span class="item__name">BBQ Chicken</span><span class="item__desc">Roast chicken, bacon, mushroom and onion on a BBQ base</span><span class="item__price">24</span></li>
  </ul>

  <h3 class="sub-title" style="top:199px">Gourmet Selections</h3>
  <ul class="menu" style="top:210px">
    <li class="item item--tall"><span class="item__num">1.</span><span class="item__name">Garlic Prawn</span><span class="item__desc">Marinated prawns, napoli sauce,<br>garlic cream sauce, mozzarella</span><span class="item__price">27</span></li>
    <li class="item item--tall"><span class="item__num">2.</span><span class="item__name">Chili Chicken</span><span class="item__desc">Marinated chicken, jalapeños, red onion,<br>buffalo sauce and mozzarella</span><span class="item__price">23</span></li>
    <li class="item item--tall"><span class="item__num">3.</span><span class="item__name">Veggie Supreme</span><span class="item__desc">Roasted pumpkin, feta, spinach,<br>caramelized onion, napoli sauce</span><span class="item__price">19</span></li>
    <li class="item item--tall"><span class="item__num">4.</span><span class="item__name">Loaded Cheeseburger</span><span class="item__desc">Sliced beef, pickle, onion, Arms special sauce,<br>mozzarella, ketchup drizzle</span><span class="item__price">23</span></li>
  </ul>

  <h3 class="sub-title" style="top:313px">Extras &amp; Add-Ons</h3>
  <ul class="menu" style="top:325px">
    <li class="item item--extra"><span class="item__num">1.</span><span class="item__name">Gluten-Free Base Available</span><span class="item__desc"></span><span class="item__price">4</span></li>
    <li class="item item--extra"><span class="item__num">2.</span><span class="item__name">Extra Cheese 3/ Extra Meat 4/ Extra Veggies</span><span class="item__desc"></span><span class="item__price">3</span></li>
    <li class="item item--extra"><span class="item__num">3.</span><span class="item__name">Side of House-Made Chilli Oil</span><span class="item__desc"></span><span class="item__price"></span></li>
    <li class="item item--extra"><span class="item__num">4.</span><span class="item__name">Pizzas Available as Half &amp; Half</span><span class="item__desc"></span><span class="item__price">2</span></li>
  </ul>

  <div class="divider" style="top:399px"></div>

  <h2 class="section-title section-title--large" style="top:416px">Kids</h2>
  <div class="sketch" style="left:382px;top:409px;width:45px;height:25px" role="img" aria-label="Line sketch of chicken nuggets"></div>
  <ul class="menu" style="top:440px">
    <li class="item"><span class="item__num">1.</span><span class="item__name">Gluten</span><span class="item__desc">Crispy nuggets with tomato sauce</span><span class="item__price">12</span></li>
    <li class="item"><span class="item__num">2.</span><span class="item__name">Kids Fish &amp; Chips</span><span class="item__desc">Battered fish fillet with tartare sauce</span><span class="item__price">12</span></li>
    <li class="item"><span class="item__num">3.</span><span class="item__name">Kids Schnitzel &amp; Chips</span><span class="item__desc">Small chicken schnitzel, gravy</span><span class="item__price">12</span></li>
    <li class="item"><span class="item__num">4.</span><span class="item__name">Cheesey Cheese Pasta</span><span class="item__desc">Creamy cheese sauce, topped with parmesan</span><span class="item__price">12</span></li>
    <li class="item"><span class="item__num">5.</span><span class="item__name">Kids Spaghetti Bolognese</span><span class="item__desc">House-made beef bolognese, parmesan</span><span class="item__price">12</span></li>
  </ul>

  <div class="divider" style="top:514px"></div>

  <h2 class="section-title section-title--large" style="top:539px">Desserts</h2>
  <div class="sketch" style="left:389px;top:518px;width:36px;height:43px" role="img" aria-label="Line sketch of a sundae cup"></div>
  <ul class="menu" style="top:567px">
    <li class="item"><span class="item__num">1.</span><span class="item__name">Chef's Special Dessert</span><span class="item__desc">Rotating seasonal selection</span><span class="item__price">12</span></li>
    <li class="item"><span class="item__num">2.</span><span class="item__name">Sticky Date Pudding</span><span class="item__desc">Butterscotch sauce, whipped cream</span><span class="item__price">12</span></li>
    <li class="item"><span class="item__num">3.</span><span class="item__name">New York Cheesecake</span><span class="item__desc">With berry compote</span><span class="item__price">12</span></li>
    <li class="item"><span class="item__num">4.</span><span class="item__name">Apple Pie</span><span class="item__desc">With ice cream</span><span class="item__price">12</span></li>
  </ul>
</section>

</body>
</html>
```